Web design for a Crane & Heavy Equipment Inspection, Repair and Maintenance Company in Texas

We need a web design for a new company based in Houston, Texas called "Kelder Crane & Equipment". We inspect, repair and maintain diesel driven heavy equipment, generators, fire water pumps and cranes. We would like to see designs that use the colors orange, white, yellow and brown, and/or orange, white, navy, yellow and grey.

```html
<!DOCTYPE html>
<html lang="en">
<head>
<meta charset="utf-8">
<title>Kelder Crane &amp; Equipment</title>
<link href="https://fonts.googleapis.com/css2?family=Ubuntu:wght@400;500;700&family=Open+Sans:wght@400;600&family=Roboto+Condensed:wght@400;700&display=swap" rel="stylesheet">
<style>
:root{
  --orange:#e8570b;
  --orange-dark:#c9470a;
  --orange-bright:#f68b0a;
  --stripe-1:#f08a2a;
  --stripe-2:#f6a630;
  --stripe-3:#f9c92e;
  --navy:#1c2f4e;
  --brown:#6b3a0b;
  --brown-title:#5a2f08;
  --text:#777;
  --dark:#333;
  --page:#f1f1f1;
  --white:#fff;
}
*{box-sizing:border-box;margin:0;padding:0}
html,body{width:1200px;height:2266px;overflow:hidden}
body{background:var(--page);font-family:"Open Sans",sans-serif;color:var(--text);position:relative}
.abs{position:absolute}
.wrap{position:absolute;left:80px;width:1040px}

.topbar{top:0;height:36px;display:flex;align-items:center;justify-content:space-between;font-size:12px;color:#555}
.topbar .info{display:flex;gap:20px;align-items:center}
.topbar .info span{display:flex;align-items:center;gap:6px}
.social-top{display:flex;gap:22px}
.social-top i{display:block;width:10px;height:10px;border-radius:50%;background:#333}

.header{top:36px;height:124px;background:var(--white);display:flex;align-items:center;justify-content:space-between;padding:0 20px 0 44px}
.brand{display:flex;align-items:center;gap:12px;font-family:"Ubuntu",sans-serif;font-weight:700;font-size:30px;color:var(--orange)}
.brand i{width:22px;height:22px;background:var(--orange)}
.contact-cta{text-align:right;font-family:"Roboto Condensed",sans-serif}
.contact-cta h3{font-weight:400;font-size:22px;color:#444;letter-spacing:.5px}
.contact-cta p{font-size:15px;color:#444;margin-top:6px}

.nav{top:160px;height:48px;background:var(--orange);display:flex;align-items:center}
.nav .home{width:50px;height:48px;background:var(--orange-dark);display:flex;align-items:center;justify-content:center}
.nav ul{list-style:none;display:flex;margin-left:26px;gap:0}
.nav li{font-family:"Roboto Condensed",sans-serif;font-size:12.5px;color:var(--white);padding:0 18px;letter-spacing:.3px}
.nav .search{margin-left:auto;width:240px;height:48px;background:var(--orange-dark);display:flex;align-items:center;justify-content:space-between;padding:0 16px;font-size:12px;color:#f5c3a0}

.hero{top:208px;height:310px;background:linear-gradient(180deg,#5d8fcf 0%,#a9c7e8 45%,#dfe6ee 62%,#9aa0a6 80%,#6f7276 100%)}
.hero-text{position:absolute;left:60px;top:92px;color:var(--navy)}
.hero-text h1{font-family:"Ubuntu",sans-serif;font-weight:700;font-size:32px}
.hero-text p{font-size:11px;line-height:15px;color:#1c2f4e;width:330px;margin-top:6px}
.btn-light{position:absolute;left:60px;top:200px;width:108px;height:38px;background:var(--white);font-family:"Roboto Condensed",sans-serif;font-size:13px;color:#555;display:flex;align-items:center;justify-content:center}

.card{top:530px;width:334px;height:420px}
.card .panel{position:absolute;top:66px;left:0;right:0;bottom:0;background:var(--white);box-shadow:0 6px 8px rgba(0,0,0,.12)}
.card .stripe{position:absolute;top:66px;left:0;right:0;height:10px}
.card .badge{position:absolute;left:103px;top:0;width:128px;height:128px;border-radius:50%;background:var(--white);box-shadow:0 0 0 4px #f3f3f3,0 2px 6px rgba(0,0,0,.15);display:flex;align-items:center;justify-content:center}
.card h2{position:absolute;top:196px;width:100%;text-align:center;font-family:"Ubuntu",sans-serif;font-weight:700;font-size:21px;color:var(--brown-title)}
.card p{position:absolute;top:234px;left:40px;right:40px;text-align:center;font-size:11px;line-height:18px}
.btn-outline{position:absolute;top:330px;left:118px;width:98px;height:40px;border:2px solid var(--stripe-1);color:var(--stripe-1);font-family:"Roboto Condensed",sans-serif;font-weight:700;font-size:16px;display:flex;align-items:center;justify-content:center}

.about{top:984px;height:398px;background:var(--white);border:1px solid #e3e3e3}
.about-photo{position:absolute;left:70px;top:38px;width:424px;height:316px;border:6px solid #ddd;background:linear-gradient(160deg,#4e7fb4 0%,#8fb5d8 50%,#c9d9e6 100%)}
.about-body{position:absolute;left:540px;top:50px;width:450px}
.about-body h2{font-family:"Ubuntu",sans-serif;font-weight:700;font-size:18px;color:var(--brown-title)}
.about-body p{font-size:11px;line-height:19px;margin-top:14px}
.btn-solid{margin-top:22px;width:92px;height:34px;background:var(--orange);color:var(--white);font-family:"Roboto Condensed",sans-serif;font-size:11px;display:flex;align-items:center;justify-content:center}

.features{top:1428px;height:402px;background:var(--orange-bright);color:var(--white)}
.features h2{position:absolute;top:46px;width:100%;text-align:center;font-family:"Roboto Condensed",sans-serif;font-weight:400;font-size:24px;letter-spacing:.5px}
.features .rule{position:absolute;top:88px;left:440px;width:160px;height:2px;background:var(--white)}
.features .rule i{position:absolute;left:76px;top:-3px;width:8px;height:8px;background:var(--white)}
.feature{position:absolute;top:142px;width:320px;text-align:center}
.feature .ring{width:96px;height:96px;border:2px solid var(--white);border-radius:50%;margin:0 auto;display:flex;align-items:center;justify-content:center}
.feature .ring span{width:60px;height:60px;border-radius:50%;background:var(--white);display:flex;align-items:center;justify-content:center}
.feature h3{font-family:"Roboto Condensed",sans-serif;font-weight:700;font-size:20px;margin-top:20px}
.feature p{font-size:11px;line-height:18px;margin:8px 20px 0}

.footer{top:1878px;height:302px}
.col{position:absolute;top:46px;width:240px}
.col h4{font-family:"Roboto Condensed",sans-serif;font-weight:400;font-size:17px;color:#333;margin-bottom:18px}
.col p{font-size:11px;line-height:18px}
.post-title{display:block;font-size:11.5px;line-height:16px;color:var(--orange-bright)}
.post-date{display:block;font-size:10px;line-height:14px;color:#555;margin:3px 0 14px}
.col .line{font-size:12px;color:#444;line-height:26px}
.col .line b{color:var(--orange-bright);font-weight:400}
.col ul{list-style:none}
.col li{font-size:11.5px;color:var(--orange-bright);line-height:20px}
.social-sq{display:flex;gap:6px;margin-top:28px}
.social-sq i{width:24px;height:24px;background:#aaa}

.bottom{top:2180px;left:0;width:1200px;height:86px;background:var(--brown);color:var(--white);font-size:11px;padding-left:88px;display:flex;align-items:center}
</style>
</head>
<body>

<div class="wrap topbar">
  <div class="info">
    <span><svg width="10" height="12" viewBox="0 0 10 12"><path d="M5 0a4 4 0 0 1 4 4c0 3-4 8-4 8S1 7 1 4a4 4 0 0 1 4-4z" fill="#333"/><circle cx="5" cy="4" r="1.5" fill="#fff"/></svg>820 Brennan Way, Houston</span>
    <span><svg width="13" height="10" viewBox="0 0 13 10"><rect width="13" height="10" fill="#333"/><path d="M0 0l6.5 5L13 0" stroke="#fff" fill="none"/></svg>info@keldercrane.test</span>
  </div>
  <div class="social-top"><i></i><i></i><i></i><i></i><i></i></div>
</div>

<header class="wrap header">
  <div class="brand"><i></i>Kelder Crane &amp; Equipment</div>
  <div class="contact-cta">
    <h3>ANY QUESTIONS?</h3>
    <p><svg width="12" height="12" viewBox="0 0 12 12"><path d="M2 1l2 0 1 3-1.5 1a7 7 0 0 0 3.5 3.5L8 7l3 1v2a1 1 0 0 1-1 1C5 11 1 7 1 2a1 1 0 0 1 1-1z" fill="#e8570b"/></svg> +1 713 555 0148</p>
  </div>
</header>

<nav class="wrap nav">
  <div class="home"><svg width="16" height="14" viewBox="0 0 16 14"><path d="M8 0l8 7h-2v7h-4V9H6v5H2V7H0z" fill="#fff"/></svg></div>
  <ul><li>SERVICES</li><li>CUSTOMER CARE</li><li>ABOUT US</li><li>CLIENTS</li><li>SITEMAP</li><li>FAQ'S</li><li>CONTACT US</li></ul>
  <div class="search">Search...<svg width="12" height="12" viewBox="0 0 12 12"><circle cx="5" cy="5" r="3.8" stroke="#fff" stroke-width="1.8" fill="none"/><path d="M8 8l3 3" stroke="#fff" stroke-width="2"/></svg></div>
</nav>

<section class="wrap hero" role="img" aria-label="Yellow mobile crane parked on a yard under a blue sky">
  <div class="hero-text">
    <h1>We Inspect &amp; Repair</h1>
    <p>repair and maintain diesel driven heavy equipment, generators, fire water pumps and cranes.</p>
  </div>
  <div class="btn-light">GET START</div>
</section>

<svg width="0" height="0" style="position:absolute">
  <defs>
    <g id="crane-icon" stroke="#1b1b1b" stroke-width="4" fill="none">
      <path d="M18 58V10M26 58V10M18 10h44M10 10h8M14 4l12 6M26 10l34-6M60 10v14"/>
      <path d="M18 20l8 8M26 20l-8 8M18 34l8 8M26 34l-8 8"/>
      <rect x="54" y="24" width="12" height="8" fill="#1b1b1b"/>
      <path d="M12 58h20" stroke-width="6"/>
    </g>
  </defs>
</svg>

<article class="card abs" style="left:80px">
  <div class="panel"></div><div class="stripe" style="background:var(--stripe-1)"></div>
  <div class="badge"><svg width="72" height="64" viewBox="0 0 72 64"><use href="#crane-icon"/></svg></div>
  <h2>Heavy Equipment</h2>
  <p>We inspect, repair and maintain diesel driven heavy equipment, generators, fire water pumps and cranes. We provide vehicle recovery services and management information</p>
  <div class="btn-outline">MORE</div>
</article>
<article class="card abs" style="left:432px">
  <div class="panel"></div><div class="stripe" style="background:var(--stripe-2)"></div>
  <div class="badge"><svg width="72" height="64" viewBox="0 0 72 64"><use href="#crane-icon"/></svg></div>
  <h2>Fire Water Pumps</h2>
  <p>We inspect, repair and maintain diesel driven heavy equipment, generators, fire water pumps and cranes. We provide vehicle recovery services and management information</p>
  <div class="btn-outline" style="border-color:var(--stripe-2);color:var(--stripe-2)">MORE</div>
</article>
<article class="card abs" style="left:786px">
  <div class="panel"></div><div class="stripe" style="background:var(--stripe-3)"></div>
  <div class="badge"><svg width="72" height="64" viewBox="0 0 72 64"><use href="#crane-icon"/></svg></div>
  <h2>Heavy Cranes</h2>
  <p>We inspect, repair and maintain diesel driven heavy equipment, generators, fire water pumps and cranes. We provide vehicle recovery services and management information</p>
  <div class="btn-outline" style="border-color:var(--stripe-3);color:var(--stripe-3)">MORE</div>
</article>

<section class="wrap about">
  <div class="about-photo" role="img" aria-label="Tower cranes rising against a blue sky"></div>
  <div class="about-body">
    <h2>Welcome to Kelder Crane &amp; Equipment</h2>
    <p>We inspect, repair and maintain diesel driven heavy equipment, generators, fire water pumps and cranes. We provide vehicle recovery services and management information services to customers, maximizing effective use of the assets.</p>
    <p>We provide vehicle recovery services and management information services to customers, maximizing effective use of the assets.</p>
    <p>A well managed fleet increases productivity and reduces cost and time. We offer M2M communication using terrestrial, satellite networks for various customized applications.</p>
    <div class="btn-solid">READ MORE</div>
  </div>
</section>

<section class="wrap features">
  <h2>CORE FEATURES</h2>
  <div class="rule"><i></i></div>
  <div class="feature" style="left:24px">
    <div class="ring"><span><svg width="22" height="22" viewBox="0 0 22 22"><path d="M20 2L9 9l4 4zM9 9l-6 2 3 2zM13 13l-2 6-2-3z" fill="#f68b0a"/></svg></span></div>
    <h3>INSPECT</h3>
    <p>We inspect, repair and maintain diesel driven heavy equipment, generators, fire water pumps and cranes. We provide vehicle recovery services and management information</p>
  </div>
  <div class="feature" style="left:360px">
    <div class="ring"><span><svg width="22" height="22" viewBox="0 0 22 22"><path d="M3 19L15 7" stroke="#f68b0a" stroke-width="3"/><path d="M17 2l1 3 3 1-3 1-1 3-1-3-3-1 3-1z" fill="#f68b0a"/></svg></span></div>
    <h3>REPAIR</h3>
    <p>We inspect, repair and maintain diesel driven heavy equipment, generators, fire water pumps and cranes. We provide vehicle recovery services and management information</p>
  </div>
  <div class="feature" style="left:696px">
    <div class="ring"><span><svg width="22" height="22" viewBox="0 0 22 22"><rect x="3" y="8" width="16" height="4" fill="#f68b0a"/><rect x="4" y="12" width="14" height="8" fill="#f68b0a"/><path d="M11 8v12" stroke="#fff" stroke-width="2"/></svg></span></div>
    <h3>MAINTAIN</h3>
    <p>We inspect, repair and maintain diesel driven heavy equipment, generators, fire water pumps and cranes. We provide vehicle recovery services and management information</p>
  </div>
</section>

<footer class="wrap footer">
  <div class="col" style="left:0">
    <h4>ABOUT US</h4>
    <p>We inspect, repair and maintain diesel driven heavy equipment, generators, fire water pumps and cranes. We provide vehicle recovery services and management information services to customers, maximizing effective use of the assets.</p>
    <div class="social-sq"><i></i><i></i><i></i><i></i><i></i><i></i></div>
  </div>
  <div class="col" style="left:266px">
    <h4>LATEST POST</h4>
    <span class="post-title">Nulla sit amet lacus non velit</span><span class="post-date">Written on 06 January 2014</span>
    <span class="post-title">Aenean quis lectus justo</span><span class="post-date">Written on 06 January 2014</span>
    <span class="post-title">Vivamus tincidunt felis nunc volut</span><span class="post-date">Written on 06 January 2014</span>
  </div>
  <div class="col" style="left:532px;width:260px">
    <h4>GET IN TUCH</h4>
    <div class="line">Phone No : +1 713 555 0172</div>
    <div class="line">Fax No : +1 713 555 0190</div>
    <div class="line">Email : info@keldercrane.test</div>
    <div class="line">Website : <b>www.keldercrane.test</b></div>
    <div class="line">Address : Kelder Yard, Suite 111, Houston</div>
  </div>
  <div class="col" style="left:800px">
    <h4>USEFUL LINK</h4>
    <ul><li>Our Privacy Policy</li><li>Kelder Portfolio</li><li>About Us</li><li>Customer Support</li><li>Help Line</li></ul>
  </div>
</footer>

<div class="abs bottom">Copyrights 2014. All Rights Reserved &nbsp;|&nbsp; Privacy Policy</div>

</body>
</html>
```